Business Cards for a company that provides webstore services to veterinarians

We need business cards designed for our main service PawCartHub. PawCartHub is a webstore that veterinarian clinics can use to that will allow their clients to purchase products for their pets. Our company is Brindlow Veterinary Solutions (BVS). Our mission statement is We love pets! We will do everything possible to facilitate along, healthy and happy relationship with their families.

Target Market(s)

Veterinarians

Industry/Entity Type

Veterinary

Contact Information for Business Card

I would like the design to incorporate the colours our our company. Cards should have room for employee name, title (only necessary in two instances), phone number, mobile number, email address and linkedin symbol and related profile name ie Marla Quinton. I would like the PawCartHub logo to appear on one side and BVS logo to appear on the other. I will need both an english and french version. I can provide the french translation. Please focus on english version and then we will translate

Colors

Designer to choose colors to be used in the design.

Requirements
Must have
• one side - PawCartHub logo with persons name, phone number, mobile number, email address
• second side - BVS logo
• colours should be consistent with our company. colours are as follows:
• Red
• RGB: 190 / 30 / 45
• CYMK: 14 / 100 / 90 /10
• Hex: #BE1E2D
• Gray
• RGB: 88 / 89 / 86
• CYMK: 3 / 2 / 0 /64
• Hex: #585956
Nice to have
• address of company - can be on either side address is 4817 Feldmoor Street Suite 305 Burlington ON K2R 6T4. Toll free number will vary depending on person
• Linkedin symbol and name of person
• on second side with BVS logo our company's mission statement
Should not have
• nothing comes to mind

```html
<!DOCTYPE html>
<html lang="en">
<head>
<meta charset="utf-8">
<title>PawCartHub / Brindlow Veterinary Solutions business cards</title>
<link rel="stylesheet" href="https://fonts.googleapis.com/css2?family=Arimo:wght@400;700&display=swap">
<style>
  :root {
    --brand-red: #be1e2d;
    --brand-gray: #585956;
    --paper: #ffffff;
    --backdrop: #e6e6e6;
  }
  * { box-sizing: border-box; margin: 0; padding: 0; }
  html, body { width: 1200px; height: 1200px; overflow: hidden; }
  body {
    background: var(--backdrop);
    font-family: "Arimo", Arial, sans-serif;
    position: relative;
  }
  .card {
    position: absolute;
    left: 390px;
    width: 420px;
    height: 252px;
    background: var(--paper);
    overflow: hidden;
    text-align: center;
  }
  .card--front { top: 266px; }
  .card--back { top: 620px; }

  .wordmark {
    position: absolute;
    top: 52px; left: 0; right: 0;
    font-size: 38px;
    line-height: 44px;
    font-weight: 400;
    color: var(--brand-gray);
  }
  .contact {
    position: absolute;
    top: 117px; left: 0; right: 0;
    color: var(--brand-red);
    font-size: 10.5px;
    line-height: 12.5px;
  }
  .contact__name { font-size: 13.5px; font-weight: 700; line-height: 16px; }
  .contact__title { color: var(--brand-gray); }
  .contact__email { margin-bottom: 12px; }

  .front-band { position: absolute; left: 0; bottom: 0; width: 420px; height: 22px; }
  .profile {
    position: absolute;
    left: 14px; bottom: 4px;
    display: flex; align-items: center; gap: 6px;
    color: var(--paper);
    font-size: 11px;
    line-height: 13px;
  }
  .profile__dot { width: 10px; height: 10px; border-radius: 50%; background: var(--paper); }

  .company-dot {
    position: absolute;
    top: 46px; left: 50%;
    width: 40px; height: 40px;
    margin-left: -20px;
    border-radius: 50%;
    background: var(--brand-red);
  }
  .company-name {
    position: absolute;
    top: 104px; left: 0; right: 0;
    font-size: 22px;
    line-height: 28px;
    font-weight: 400;
    color: var(--brand-red);
  }
  .mission {
    position: absolute;
    top: 208px; left: 0; right: 0;
    font-size: 6.5px;
    line-height: 8px;
    color: var(--brand-red);
  }
  .mission__label { color: var(--brand-gray); font-weight: 700; }
</style>
</head>
<body>

<section class="card card--front">
  <div class="wordmark">PawCartHub</div>

  <div class="contact">
    <p class="contact__name">Marla Quinton</p>
    <p class="contact__title">CEO</p>
    <p class="contact__email">info@pawcarthub.ca</p>
    <p>4817 Feldmoor Street, Suite 305</p>
    <p>Burlington, Ontario K2R 6T4 Canada</p>
    <p>P: 1-877-555-0142 &nbsp;|&nbsp; T: 1.877.555.0142</p>
    <p>F: 1.866.555.0199 | vets.pawcarthub.ca</p>
  </div>

  <svg class="front-band" viewBox="0 0 420 22" aria-hidden="true">
    <polygon points="212,0 420,0 420,4 214,4" fill="var(--brand-gray)"/>
    <polygon points="0,0 200,0 218,10 420,10 420,22 0,22" fill="var(--brand-red)"/>
  </svg>
  <div class="profile">
    <span class="profile__dot"></span>
    <span>Marla Quinton</span>
  </div>
</section>

<section class="card card--back">
  <span class="company-dot"></span>
  <div class="company-name">Brindlow Veterinary Solutions</div>
  <div class="mission">
    <p class="mission__label">company's mission statement :</p>
    <p>the needs of &nbsp;independent practices | distributors | buying groups</p>
    <p>industry associations | retail chains</p>
  </div>
</section>

</body>
</html>
```